New young doctors office business card

Doctor's office
Hello:
My name is Dr. Mateo Anselmo Quiroga Benítez. I need a business card for my new office located within a hospital. The name of the hospital is "Hospital Almendral". Although the hospital logo and name must be included in the business card, please make me a personal logo for myself. The logo might be maybe my name in a stylish font, or my initials (MAQB) or something like that. Im more inclined to a font logo, rather than a image logo, but a good one might change my mind. The info on my business card is going to be in spanish. The following info must be included please (the info within parenthesis is not to be included, it is provided for you to understand it since it's in spanish, so you can properly place it on the card):
-Dr. Mateo Anselmo Quiroga Benítez (my name)
-Medicina general (My specialty)
-Hospital Almendral (The name of the hospital where my office is)
-Calle Tomás Ibarrola #527 Col. Peñascal (address)
-Tel 471-5836 (Office phone)
-Sábado y domingo 10:00 am a 10:00pm (Office hours)
-Emergencias: 613-907-5148 (Emergency phone)
-mateoqb@correoandino.net (email)
-English Spoken
So, that's all the info i need to be on the business card. Although it's a business card for a doctor's office, i dont want it to be a boring, plain business card. Make it eye-catchy and stylish please. As i said, the hospital logo must be included. You'll find it on the heading of the PDF file i attached, but dont make it the center of attention.
Physician
Hello:My name is Dr. Mateo Anselmo Quiroga Benítez. I need a business card for my new office located within a hospital. The name of the hospital is "Hospital Almendral". Although the hospital logo and name must be included in the business card, please make me a personal logo for myself. The logo might be maybe my name in a stylish font, or my initials (MAQB) or something like that. Im more inclined to a font logo, rather than a image logo, but a good one might change my mind. The info on my business card is going to be in spanish. The following info must be included please (the info within parenthesis is not to be included, it is provided for you to understand it since it's in spanish, so you can properly place it on the card):-Dr. Mateo Anselmo Quiroga Benítez (my name)-Medicina general (My specialty)-Hospital Almendral (The name of the hospital where my office is)-Calle Tomás Ibarrola #527 Col. Peñascal (address)-Tel 471-5836 (Office phone)-Sábado y domingo 10:00 am a 10:00pm (Office hours)-Emergencias: 613-907-5148 (Emergency phone)-mateoqb@correoandino.net (email)-English Spoken So, that's all the info i need to be on the business card. Although it's a business card for a doctor's office, i dont want it to be a boring, plain business card. Make it eye-catchy and stylish please. As i said, the hospital logo must be included. You'll find it on the heading of the PDF file i attached, but dont make it the center of attention.

```html
<!DOCTYPE html>
<html lang="es">
<head>
<meta charset="utf-8">
<title>Tarjeta de presentación — Dr. MAQB</title>
<link href="https://fonts.googleapis.com/css2?family=Cabin:ital,wght@0,400;0,600;0,700;1,700&display=swap" rel="stylesheet">
<style>
  :root {
    --bg: #2b323d;
    --paper: #ffffff;
    --navy: #27303e;
    --navy-light: #3a4658;
    --band: rgba(80,110,140,.35);
    --brand-blue: #1a2fa8;
    --lime: #8ee83a;
    --aqua: #aef7fb;
    --aqua-text: #9eeef6;
    --ink-light: #ffffff;
    --font: "Cabin", sans-serif;
  }
  * { box-sizing: border-box; margin: 0; padding: 0; }
  html, body { width: 1200px; height: 1200px; overflow: hidden; }
  body { background: var(--bg); font-family: var(--font); position: relative; }

  .card {
    position: absolute; left: 200px; width: 800px; height: 457px;
    overflow: hidden; box-shadow: 0 14px 30px rgba(0,0,0,.45);
  }
  .card--front { top: 90px; background: var(--paper); }
  .card--back { top: 640px; background: var(--navy); }

  .hospital-name {
    font-family: var(--font); font-weight: 600; color: var(--brand-blue);
    font-size: 19px; white-space: nowrap;
  }
  .doctor-name-mark {
    font-family: var(--font); font-weight: 600; color: var(--brand-blue);
    line-height: 1; white-space: nowrap;
  }

  /* Front */
  .front__hospital { position: absolute; top: 60px; left: 0; right: 0; text-align: center; }
  .front__mark { position: absolute; top: 168px; left: 0; right: 0; text-align: center; font-size: 72px; }
  .front__rule { position: absolute; left: 80px; right: 80px; top: 262px; height: 3px; background: var(--lime); }
  .front__band {
    position: absolute; left: 0; right: 0; bottom: 0; height: 178px;
    background: linear-gradient(100deg, var(--navy) 0%, var(--navy-light) 100%);
  }
  .front__specialty {
    position: absolute; left: 0; right: 0; bottom: 60px; text-align: center;
    font-style: italic; font-weight: 700; font-size: 22px; color: var(--aqua-text);
  }

  /* Back */
  .back__panel { position: absolute; left: 22px; top: 0; bottom: 0; width: 340px; background: var(--paper); }
  .back__contact-band { position: absolute; left: 362px; right: 0; top: 244px; height: 104px; background: var(--band); }
  .back__aqua {
    position: absolute; left: 22px; top: 192px; height: 130px; width: 480px;
    background: linear-gradient(90deg, var(--aqua) 0, var(--aqua) 318px, rgba(174,247,251,.4) 340px, rgba(174,247,251,0) 480px);
  }
  .back__stripe { position: absolute; left: 0; top: 0; bottom: 0; width: 22px; background: var(--lime); }
  .back__mark { position: absolute; left: 22px; width: 340px; top: 72px; text-align: center; font-size: 56px; }
  .back__hospital { position: absolute; left: 22px; width: 340px; bottom: 48px; text-align: center; }
  .back__info {
    position: absolute; right: 50px; top: 48px; width: 430px;
    text-align: right; color: var(--ink-light); font-size: 20px; line-height: 1.3;
  }
  .back__info .specialty { color: var(--aqua-text); font-weight: 700; font-size: 22px; }
  .back__info .group { margin-top: 22px; }
  .back__info .english { margin-top: 66px; }
</style>
</head>
<body>
  <section class="card card--front" aria-label="Frente de la tarjeta">
    <div class="front__hospital"><span class="hospital-name">Hospital Almendral</span></div>
    <div class="front__mark"><span class="doctor-name-mark">MAQB</span></div>
    <div class="front__band"></div>
    <div class="front__rule"></div>
    <p class="front__specialty">Medicina general</p>
  </section>

  <section class="card card--back" aria-label="Reverso de la tarjeta">
    <div class="back__panel"></div>
    <div class="back__contact-band"></div>
    <div class="back__aqua"></div>
    <div class="back__stripe"></div>
    <div class="back__mark"><span class="doctor-name-mark">MAQB</span></div>
    <div class="back__hospital"><span class="hospital-name">Hospital Almendral</span></div>
    <div class="back__info">
      <p>Dr. Mateo Anselmo Quiroga Benítez</p>
      <p class="specialty">Medicina general</p>
      <div class="group">
        <p>Hospital Almendral</p>
        <p>Calle Tomás Ibarrola #527 Col. Peñascal</p>
      </div>
      <div class="group">
        <p>Tel: 471-5836</p>
        <p>Sábado y domingo 10:00 am a 10:00pm</p>
        <p>Emergencias: 613-907-5148</p>
        <p>mateoqb@correoandino.net</p>
      </div>
      <p class="english">English Spoken</p>
    </div>
  </section>
</body>
</html>
```